The Harbor Post - Built for the Industry, by the Industry.

Looking for an email marketing Infographic I can send out via email to target Recruitment Firms letting them know we are launched! As of January 7th VALOKA is no longer allowing Recruitment Firms to post on their site unless you pay thousands of dollars a month. We are launching a site just for Recruiters to showcase their jobs. I have attached the almost completed website and a mocked up version of a simple infographic but we are looking for a WOW design that can get emailed out to 1000's of Recruitment Firms and they will just have to click the image to be taken to our site. I have added the colors and raleway - medium is the font on our site. Blue RGB: 8/113/182 Navy RGB: 27/32/48

Target Market(s)

Recruitment Firms Across Canada and the USA

Font styles to use
Other font styles liked:
• Very Open ...

Requirements
Must have
• WOW Factor, use of our Brand and Colours - raleway - medium is the font on our site. Blue RGB: 8/113/182 Navy RGB: 27/32/48. Our Logo and I have also attached our Landing Page ... down below.
Nice to have
• You can use "It's Time for Something New" or I'd be open to other ideas and taglines ... I'd like to see No Sponsored Jobs / No Pay-Per-Click / Flat Rates Only ...
• Our tagline is also - Built for the Industry, by the Industry"

```html
<!DOCTYPE html>
<html lang="en">
<head>
<meta charset="utf-8">
<title>The Harbor Post — It's Time for Something New</title>
<link rel="stylesheet" href="https://fonts.googleapis.com/css2?family=Raleway:wght@300;400;500;800&display=swap">
<style>
  :root {
    --navy: #1b2030;
    --navy-deep: #171b29;
    --navy-soft: #262c42;
    --blue: #0871b6;
    --orange: #f7941d;
    --white: #ffffff;
    --chair: #4a5478;
  }
  * { box-sizing: border-box; margin: 0; padding: 0; }
  html, body { width: 909px; height: 1200px; overflow: hidden; }
  body {
    font-family: "Raleway", sans-serif;
    background: radial-gradient(ellipse at 50% 35%, var(--navy-soft) 0%, var(--navy) 55%, var(--navy-deep) 100%);
    color: var(--white);
    position: relative;
  }
  .email { position: absolute; inset: 0; }
  .hero-illustration {
    position: absolute; left: 274px; top: 34px; width: 360px; height: 280px;
    background: radial-gradient(ellipse at 50% 55%, var(--chair) 0%, #343c58 45%, rgba(27,32,48,0) 72%);
  }
  .rule { position: absolute; left: 50%; transform: translateX(-50%); height: 2px; background: var(--blue); }
  .rule--top { top: 335px; width: 577px; }
  .rule--bottom { top: 687px; width: 388px; }
  .headline { position: absolute; left: 0; right: 0; text-align: center; }
  .headline__lead {
    top: 354px; font-weight: 300; font-size: 84px; line-height: 1; color: var(--orange); letter-spacing: 0.01em;
  }
  .headline__main {
    top: 432px; font-weight: 800; font-size: 68px; line-height: 1; color: var(--white); letter-spacing: -0.01em;
  }
  .perks { position: absolute; left: 0; right: 0; top: 512px; list-style: none; }
  .perk {
    height: 59px; display: flex; align-items: center; justify-content: center; gap: 14px;
    font-weight: 500; font-size: 35px; letter-spacing: 0.17em;
  }
  .perk svg { width: 34px; height: 34px; flex: none; }
  .brand {
    position: absolute; left: 0; right: 0; top: 742px;
    display: flex; align-items: center; justify-content: center; gap: 22px;
  }
  .brand__dot { width: 70px; height: 70px; border-radius: 50%; background: var(--white); flex: none; }
  .brand__name { font-weight: 500; font-size: 58px; letter-spacing: 0.06em; color: var(--white); line-height: 1; }
  .brand__tagline {
    position: absolute; left: 0; right: 0; top: 846px; text-align: center;
    font-weight: 500; font-size: 15px; letter-spacing: 0.01em;
  }
  .pitch {
    position: absolute; left: 0; right: 0; top: 896px; text-align: center;
    font-weight: 400; font-size: 18px; line-height: 22.5px; letter-spacing: 0.16em; text-transform: uppercase;
  }
  .cta {
    position: absolute; left: 50%; top: 1027px; transform: translateX(-50%);
    width: 134px; height: 134px; border: 3px solid var(--white); border-radius: 50%;
    display: flex; flex-direction: column; align-items: center; justify-content: center;
    color: var(--white); text-decoration: none; text-transform: uppercase; letter-spacing: 0.14em;
  }
  .cta__small { font-weight: 400; font-size: 18px; }
  .cta__big { font-weight: 800; font-size: 22px; }
</style>
</head>
<body>
<main class="email">
  <div class="hero-illustration" role="img" aria-label="Illustration of an office chair carrying a sign reading Built for the Industry by the Industry, with small geometric shapes around it"></div>

  <div class="rule rule--top"></div>
  <h1>
    <span class="headline headline__lead">IT'S TIME FOR</span>
    <span class="headline headline__main">SOMETHING NEW</span>
  </h1>

  <ul class="perks">
    <li class="perk">
      <svg viewBox="0 0 34 34" fill="none" stroke="var(--orange)" stroke-width="2"><circle cx="15" cy="15" r="12"/><line x1="7" y1="7" x2="23" y2="23"/><path d="M9 13h4l7-4v12l-7-4H9z"/><circle cx="26" cy="26" r="6" fill="var(--navy)"/><text x="26" y="29.5" font-size="9" text-anchor="middle" fill="var(--orange)" stroke="none" font-family="Raleway, sans-serif">$</text></svg>
      No sponsored jobs
    </li>
    <li class="perk">
      <svg viewBox="0 0 34 34" fill="none" stroke="var(--orange)" stroke-width="2"><circle cx="17" cy="17" r="13"/><line x1="8" y1="8" x2="26" y2="26"/><rect x="13" y="10" width="8" height="13" rx="4"/><line x1="17" y1="10" x2="17" y2="15"/></svg>
      No pay-per-click
    </li>
    <li class="perk">
      <svg viewBox="0 0 34 34" fill="none" stroke="var(--orange)" stroke-width="2"><rect x="8" y="3" width="18" height="28"/><text x="17" y="15" font-size="10" text-anchor="middle" fill="var(--orange)" stroke="none" font-family="Raleway, sans-serif">$</text><line x1="11" y1="20" x2="23" y2="20"/><line x1="11" y1="24" x2="23" y2="24"/><line x1="11" y1="28" x2="23" y2="28"/></svg>
      Flat rates only
    </li>
  </ul>
  <div class="rule rule--bottom"></div>

  <div class="brand">
    <span class="brand__dot"></span>
    <span class="brand__name">THE HARBOR POST</span>
  </div>
  <p class="brand__tagline">BUILT FOR THE INDUSTRY, BY THE INDUSTRY</p>

  <p class="pitch">Let our vast network of<br>recruiters connect you<br>with your next<br>opportunity.</p>

  <a class="cta" href="#">
    <span class="cta__small">Visit us</span>
    <span class="cta__big">Today</span>
  </a>
</main>
</body>
</html>
```